New Business Cards / Logo update

Logo:
can be updated but wanted pricing

New Business Cards:
take our existing business cards and upgrade them from a design perspective. We have two versions
Inside sales team does not have a cell phone and they use an appointment back slot.
Outside project managers and leadership uses a slogan backing and will have cell phones.

```html
<!DOCTYPE html>
<html lang="en">
<head>
<meta charset="utf-8">
<title>Summit Carpet + Flooring — Business Cards</title>
<link rel="stylesheet" href="https://fonts.googleapis.com/css2?family=Libre+Baskerville&family=Roboto:wght@400;500;700&display=swap">
<style>
  :root {
    --orange: #df8a1f;
    --grey: #8f8784;
    --grey-light: #c9c5c3;
    --text-grey: #6f6a68;
    --white: #ffffff;
    --stage: #1d1d1f;
  }
  * { box-sizing: border-box; margin: 0; padding: 0; }
  html, body { width: 1200px; height: 900px; overflow: hidden; }
  body {
    background: var(--stage);
    font-family: "Roboto", Arial, sans-serif;
    display: flex;
    flex-direction: column;
    align-items: center;
    justify-content: center;
    gap: 48px;
  }
  .card {
    position: relative;
    width: 560px;
    height: 320px;
    overflow: hidden;
    background: var(--white);
    box-shadow: 0 14px 30px rgba(0,0,0,.45);
  }
  .card-art { position: absolute; inset: 0; width: 100%; height: 100%; }

  /* Front */
  .contact { position: absolute; left: 34px; top: 34px; color: var(--white); }
  .contact-name { font-family: "Libre Baskerville", Georgia, serif; font-size: 28px; line-height: 1.1; }
  .contact-title { font-size: 15px; margin-top: 4px; }
  .contact-address { font-size: 15px; line-height: 1.35; margin-top: 34px; }
  .contact-list { list-style: none; margin-top: 28px; font-size: 15px; line-height: 1.4; }
  .contact-list li { display: flex; align-items: center; gap: 7px; }
  .contact-list svg { width: 13px; height: 13px; flex: none; }
  .front-brand {
    position: absolute; right: 24px; top: 150px; width: 210px;
    color: var(--orange); font-size: 28px; font-weight: 500; line-height: 1.15; text-align: center;
  }

  /* Back */
  .back-brand {
    position: absolute; right: 30px; top: 20px;
    color: var(--white); font-size: 28px; font-weight: 500; text-align: right; line-height: 1.1;
  }
  .appointment-label {
    position: absolute; right: 62px; top: 152px;
    color: var(--orange); font-size: 24px; letter-spacing: 1px; line-height: 1;
  }
  .slot-rule { position: absolute; left: 30px; right: 30px; top: 194px; border-top: 1.5px dashed var(--grey-light); }
  .slot-row { position: absolute; left: 30px; right: 30px; top: 214px; display: flex; gap: 14px; color: var(--text-grey); font-size: 14px; letter-spacing: 1px; }
  .slot-field { display: flex; align-items: flex-end; gap: 6px; flex: 1; }
  .slot-field span.line { flex: 1; border-bottom: 1px solid var(--grey-light); height: 14px; }
  .slogan { position: absolute; left: 30px; bottom: 28px; font-size: 21px; color: var(--text-grey); }
  .slogan strong { color: var(--orange); font-weight: 700; }
</style>
</head>
<body>

  <!-- Front: contact side -->
  <section class="card card-front">
    <svg class="card-art" viewBox="0 0 560 320" aria-hidden="true">
      <rect width="560" height="320" fill="var(--orange)"/>
      <path d="M321,320 C280,228 292,110 420,80 C470,68 520,68 560,72" fill="none" stroke="var(--grey)" stroke-width="4"/>
      <path d="M332,320 C292,230 304,122 424,90 C472,78 520,78 560,82 L560,320 Z" fill="var(--white)"/>
    </svg>
    <div class="contact">
      <p class="contact-name">Dana Whitfield</p>
      <p class="contact-title">Sales + Design Manager</p>
      <p class="contact-address">1520 Harbor View Rd<br>Port Marlow, FL 34000</p>
      <ul class="contact-list">
        <li><svg viewBox="0 0 16 16"><path d="M3 1h3l1.5 4-2 1.2a9 9 0 0 0 4.3 4.3L11 8.5l4 1.5v3a2 2 0 0 1-2 2A12 12 0 0 1 1 3a2 2 0 0 1 2-2z" fill="var(--white)"/></svg>555-014-2290</li>
        <li><svg viewBox="0 0 16 16"><rect x="1" y="3" width="14" height="10" rx="1" fill="var(--white)"/><path d="M1.5 3.5 8 9l6.5-5.5" fill="none" stroke="var(--orange)" stroke-width="1.4"/></svg>dana@summitcarpetco.com</li>
        <li><svg viewBox="0 0 16 16"><circle cx="8" cy="8" r="7" fill="var(--white)"/><path d="M1 8h14M8 1c-3 3.5-3 10.5 0 14M8 1c3 3.5 3 10.5 0 14" fill="none" stroke="var(--orange)" stroke-width="1.1"/></svg>summitcarpetco.com</li>
      </ul>
    </div>
    <p class="front-brand">Summit Carpet + Flooring</p>
  </section>

  <!-- Back: appointment side -->
  <section class="card card-back">
    <svg class="card-art" viewBox="0 0 560 320" aria-hidden="true">
      <path d="M0,0 H560 V118 C400,94 200,56 0,30 Z" fill="var(--orange)"/>
      <path d="M0,42 C200,66 400,102 560,130" fill="none" stroke="var(--grey)" stroke-width="3"/>
      <path d="M60,54 C260,76 420,108 560,142" fill="none" stroke="var(--orange)" stroke-width="3.5"/>
    </svg>
    <p class="back-brand">Summit Carpet + Flooring</p>
    <p class="appointment-label">APPOINTMENT</p>
    <div class="slot-rule"></div>
    <div class="slot-row">
      <div class="slot-field">DATE:<span class="line"></span></div>
      <div class="slot-field">TIME:<span class="line"></span></div>
    </div>
    <p class="slogan"><strong>Summit</strong> flooring at an affordable price</p>
  </section>

</body>
</html>
```